Business Card for Financial Asset Management Company

Now we are launching a new company based in Tokyo.
The company information is below;

Company Name: Talvane Management

Operations: Financial assets management, Proposing forming portfolio of assets, Consulting service, and advising to enhance your company's financial health

Corporate Colour: Japan Blue or Navy like below
http://staffpages.qorvenly.edu/mtavis/images/Slate/Teal-Slate-217.jpg

It's dark and deep, and will get to fit to our clients as our relationships last longer and longer.

Our images for this colour are "Japanese style" and "pride in our craftmanship" , and also "gentle".

Corporate Key Image: an order taker who is sincere, polite, but courageous

We don't have our logo yet so please feel free to put any symbol on your design.

Please do not hesitate about asking any questions.
Thank you :-)

Reason: We are still discussin on final decision. Thank you for your understanding.

```html
<!DOCTYPE html>
<html lang="en">
<head>
<meta charset="utf-8">
<title>Talvane Management – Business Card</title>
<link href="https://fonts.googleapis.com/css2?family=Roboto+Condensed:wght@400;700&display=swap" rel="stylesheet">
<style>
  :root {
    --navy: #14164a;
    --navy-deep: #0b0c33;
    --navy-text: #23246e;
    --silver: #c9ccd6;
    --grey-name: #8c8c8c;
    --backdrop: #eceae6;
    --card-white: #ffffff;
    --photo-light: #d9d9dc;
    --photo-dark: #3a3b4a;
  }
  * { box-sizing: border-box; margin: 0; padding: 0; }
  html, body { width: 1200px; height: 784px; overflow: hidden; }
  body {
    background: var(--backdrop);
    font-family: "Roboto Condensed", Arial, sans-serif;
    position: relative;
  }
  .card {
    position: absolute;
    width: 540px;
    height: 309px;
    top: 238px;
    border-radius: 3px;
    box-shadow: 0 6px 18px rgba(0,0,0,0.18);
    overflow: hidden;
  }
  /* Back of card */
  .card-back {
    left: 40px;
    background: radial-gradient(ellipse at 50% 35%, #23266a 0%, var(--navy) 45%, var(--navy-deep) 100%);
  }
  .back-brand {
    position: absolute;
    left: 0; right: 0; top: 70px;
    display: flex; flex-direction: column; align-items: center;
  }
  .back-mark {
    width: 92px; height: 92px;
    background: var(--silver);
    border-radius: 16px;
  }
  .back-name {
    margin-top: 26px;
    font-size: 34px;
    font-weight: 700;
    color: var(--silver);
    letter-spacing: 0.3px;
  }
  /* Front of card */
  .card-front {
    left: 620px;
    background: var(--card-white);
  }
  .front-mark {
    position: absolute;
    left: 26px; top: 62px;
    width: 74px; height: 74px;
    background: var(--navy);
    border-radius: 12px;
  }
  .front-name {
    position: absolute;
    left: 114px; top: 62px;
    font-size: 23px;
    font-weight: 700;
    color: var(--navy-text);
  }
  .portrait {
    position: absolute;
    right: 0; top: 44px;
    width: 140px; height: 190px;
    background: linear-gradient(160deg, var(--photo-light) 0%, #9a9ba6 55%, var(--photo-dark) 100%);
  }
  .holder {
    position: absolute;
    left: 36px; top: 150px;
  }
  .holder-name { font-size: 17px; color: var(--grey-name); }
  .holder-title { font-size: 10px; color: var(--navy-text); margin-top: 1px; }
  .contacts {
    position: absolute;
    left: 30px; top: 196px;
    list-style: none;
  }
  .contacts li {
    display: flex; align-items: center;
    font-size: 13.5px;
    color: var(--navy-text);
    height: 16px;
  }
  .contacts svg { width: 12px; height: 12px; margin-right: 7px; fill: #555; flex: none; }
  .contacts .indent { padding-left: 19px; }
  .front-band {
    position: absolute;
    left: 0; right: 0; bottom: 0;
    height: 30px;
    background: linear-gradient(180deg, #1f2160, var(--navy-deep));
  }
</style>
</head>
<body>
  <section class="card card-back">
    <div class="back-brand">
      <div class="back-mark"></div>
      <div class="back-name">Talvane Management</div>
    </div>
  </section>

  <section class="card card-front">
    <div class="front-mark"></div>
    <div class="front-name">Talvane Management</div>
    <div class="portrait" role="img" aria-label="Portrait photo of the director in a dark suit holding a business card"></div>

    <div class="holder">
      <div class="holder-name">Oren Vasko</div>
      <div class="holder-title">Director</div>
    </div>

    <ul class="contacts">
      <li>
        <svg viewBox="0 0 24 24"><path d="M6.6 10.8a15 15 0 0 0 6.6 6.6l2.2-2.2c.3-.3.7-.4 1-.2 1.1.4 2.3.6 3.6.6.6 0 1 .4 1 1V20c0 .6-.4 1-1 1A17 17 0 0 1 3 4c0-.6.4-1 1-1h3.5c.6 0 1 .4 1 1 0 1.3.2 2.5.6 3.6.1.3 0 .7-.2 1z"/></svg>
        1562 417 903
      </li>
      <li>
        <svg viewBox="0 0 24 24"><path d="M12 2a10 10 0 1 0 0 20 10 10 0 0 0 0-20zm6.9 6h-2.9a15 15 0 0 0-1.4-3.6A8 8 0 0 1 18.9 8zM12 4c.8 1.2 1.5 2.5 1.9 4h-3.8c.4-1.5 1.1-2.8 1.9-4zM4.3 14a8 8 0 0 1 0-4h3.4a16 16 0 0 0 0 4zm.8 2h2.9c.3 1.3.8 2.5 1.4 3.6A8 8 0 0 1 5.1 16zM8 8H5.1a8 8 0 0 1 4.3-3.6C8.8 5.5 8.3 6.7 8 8zm4 12c-.8-1.2-1.5-2.5-1.9-4h3.8c-.4 1.5-1.1 2.8-1.9 4zm2.3-6H9.7a14 14 0 0 1 0-4h4.6a14 14 0 0 1 0 4zm.3 5.6c.6-1.1 1.1-2.3 1.4-3.6h2.9a8 8 0 0 1-4.3 3.6zm1.7-5.6a16 16 0 0 0 0-4h3.4a8 8 0 0 1 0 4z"/></svg>
        www.talvanemgmt.com
      </li>
      <li>
        <svg viewBox="0 0 24 24"><path d="M3 5h18c.6 0 1 .4 1 1v12c0 .6-.4 1-1 1H3c-.6 0-1-.4-1-1V6c0-.6.4-1 1-1zm1 2.4V17h16V7.4l-8 5.3z"/></svg>
        oren@talvanemgmt.com
      </li>
      <li>
        <svg viewBox="0 0 24 24"><path d="M12 3l10 9h-3v8h-5v-6h-4v6H5v-8H2z"/></svg>
        482C Harwick Street, Tamsbury 6012
      </li>
      <li class="indent">PO Box 529 Tamsbury 6918</li>
    </ul>

    <div class="front-band"></div>
  </section>
</body>
</html>
```